We are in search of a new business card design for our business. We have a Mexican Grocery Store called Tortilla Grove Market, we would like to see that some have mexican design, but we are open to any type of designs.

Phone: to be announced
Fax: to be announced

Address is:
2415 Calloway Blvd
Larkdale, MD 21230

```html
<!DOCTYPE html>
<html lang="en">
<head>
<meta charset="UTF-8">
<title>Tortilla Grove Market – Business Card</title>
<link href="https://fonts.googleapis.com/css2?family=Roboto:wght@500;700&display=swap" rel="stylesheet">
<style>
  :root {
    --backdrop: #6b5643;
    --card: #ebd38b;
    --band: #c9c48e;
    --band-light: #ece6a8;
    --ink: #333333;
    --accent-red: #a3161b;
    --icon-green: #2f7d4f;
    --brand: #b3281f;
  }
  * { margin: 0; padding: 0; box-sizing: border-box; }
  html, body {
    width: 1200px;
    height: 900px;
    overflow: hidden;
    background: var(--backdrop);
    font-family: "Roboto", Arial, sans-serif;
  }
  .business-card {
    position: absolute;
    left: 135px;
    top: 177px;
    width: 930px;
    height: 543px;
    background: var(--card);
    box-shadow: 0 6px 18px rgba(0, 0, 0, 0.35);
  }
  .side-band {
    position: absolute;
    top: 0;
    width: 57px;
    height: 100%;
    background: linear-gradient(90deg, var(--band-light), var(--band), var(--band-light));
  }
  .side-band--left { left: 0; }
  .side-band--right { right: 0; }
  .holder {
    position: absolute;
    left: 99px;
    top: 76px;
  }
  .holder__name {
    font-size: 38px;
    font-weight: 700;
    color: var(--ink);
    line-height: 1;
  }
  .holder__role {
    margin-top: 9px;
    font-size: 22px;
    font-weight: 500;
    color: var(--accent-red);
    line-height: 1;
  }
  .brand {
    position: absolute;
    left: 490px;
    top: 118px;
    width: 340px;
    display: flex;
    align-items: center;
    gap: 14px;
  }
  .brand__dot {
    flex: none;
    width: 34px;
    height: 34px;
    border-radius: 50%;
    background: var(--icon-green);
  }
  .brand__name {
    font-size: 38px;
    font-weight: 700;
    color: var(--brand);
    line-height: 1.1;
  }
  .contact-lines {
    position: absolute;
    left: 95px;
    top: 410px;
    list-style: none;
  }
  .contact-lines li {
    display: flex;
    align-items: center;
    gap: 12px;
    height: 32px;
    font-size: 25px;
    font-weight: 500;
    color: var(--ink);
  }
  .contact-lines svg { width: 24px; height: 22px; fill: var(--icon-green); }
  .address {
    position: absolute;
    left: 586px;
    top: 410px;
    font-style: normal;
    font-size: 25px;
    font-weight: 500;
    line-height: 32px;
    color: var(--ink);
  }
</style>
</head>
<body>
  <section class="business-card">
    <div class="side-band side-band--left" role="img" aria-label="Zigzag chevron border pattern in olive and cream"></div>
    <div class="side-band side-band--right" role="img" aria-label="Zigzag chevron border pattern in olive and cream"></div>

    <header class="holder">
      <h1 class="holder__name">Marco Reyes</h1>
      <p class="holder__role">Owner</p>
    </header>

    <div class="brand">
      <span class="brand__dot"></span>
      <span class="brand__name">Tortilla Grove Market</span>
    </div>

    <ul class="contact-lines">
      <li>
        <svg viewBox="0 0 24 22" aria-hidden="true">
          <path d="M2 6c0-3 4-5 10-5s10 2 10 5v2h-5V6c-1-1-3-1.5-5-1.5S8 5 7 6v2H2z"/>
          <path d="M5 10h14l2 10H3z M12 12.5a3.5 3.5 0 1 0 0.01 0z" fill-rule="evenodd"/>
        </svg>
        <span>045-871-209</span>
      </li>
      <li>
        <svg viewBox="0 0 24 22" aria-hidden="true">
          <rect x="6" y="1" width="12" height="6"/>
          <path d="M2 8h20v9h-4v-4H6v4H2z"/>
          <rect x="7" y="14" width="10" height="7"/>
        </svg>
        <span>234-615-782</span>
      </li>
    </ul>

    <address class="address">
      2415 Calloway Blvd<br>
      Larkdale, MD 21230
    </address>
  </section>
</body>
</html>
```